Hi,
We are an accounting firm looking to upgrade the following:
Logo, letterhead, withcomp slips and maybe our business cards. I have attached our original letterhead (sample A) and a letterhead (SAmple B) which we like the design and layout, however I want to stick with the colours of our orginal letterhead (Sample A) but improve and modernise the look with other letter head (Sample B) I have attached both. On the footer of Sample A, we would like to remove the names of the directors but leave EST. 1985 we also want to add the QRT logo ABN and TAX AGENT logo as stated in Sample B , we would like to do a layout for the header similar to SAmple B however maybe a bit more structured.

```html
<!DOCTYPE html>
<html lang="en">
<head>
<meta charset="utf-8">
<title>Brentholm Letterhead</title>
<link href="https://fonts.googleapis.com/css2?family=Arimo:wght@400;700&display=swap" rel="stylesheet">
<style>
  :root {
    --brand-navy: #0b1766;
    --brand-blue: #0a3d9c;
    --sky-blue: #2e9bff;
    --icon-blue: #3a9cf0;
    --ink: #111111;
    --paper: #ffffff;
    --badge-red: #e31c2a;
    --badge-green: #9be11e;
  }
  html, body {
    margin: 0;
    padding: 0;
    width: 848px;
    height: 1200px;
    overflow: hidden;
    background: var(--paper);
  }
  .letterhead {
    position: relative;
    width: 848px;
    height: 1200px;
    overflow: hidden;
    background: var(--paper);
    font-family: "Arimo", Arial, sans-serif;
    color: var(--ink);
  }
  .brand {
    position: absolute;
    left: 56px;
    top: 55px;
    display: flex;
    align-items: center;
    gap: 9px;
  }
  .brand-mark {
    width: 15px;
    height: 15px;
    background: var(--brand-blue);
  }
  .brand-name {
    font-size: 35px;
    font-weight: 700;
    color: var(--brand-blue);
    letter-spacing: -0.5px;
    line-height: 1;
  }
  .contact-row {
    position: absolute;
    left: 353px;
    height: 16px;
    font-size: 11.7px;
    line-height: 1;
    white-space: nowrap;
  }
  .contact-row .item {
    position: absolute;
    top: 0;
    display: flex;
    align-items: center;
    gap: 6px;
  }
  .contact-row strong { font-weight: 700; }
  .icon {
    width: 15px;
    height: 15px;
    flex: none;
    fill: none;
    stroke: var(--icon-blue);
    stroke-width: 1.4;
    stroke-linecap: round;
    stroke-linejoin: round;
  }
  .row-address { top: 42px; }
  .row-phone { top: 72px; }
  .row-web { top: 103px; }
  .est {
    position: absolute;
    left: 51px;
    top: 1086px;
    margin: 0;
    font-size: 13.5px;
  }
  .accreditations {
    position: absolute;
    left: 648px;
    top: 1049px;
    display: flex;
    align-items: center;
    gap: 18px;
  }
  .badge-institute {
    width: 42px;
    height: 48px;
    background: var(--badge-red);
  }
  .badge-registered {
    width: 52px;
    height: 52px;
    border-radius: 50%;
    background: var(--badge-green);
  }
  .footer-band {
    position: absolute;
    left: 0;
    bottom: 0;
    width: 848px;
    height: 62px;
    background: linear-gradient(90deg, var(--brand-blue) 0%, var(--brand-navy) 55%, var(--sky-blue) 100%);
  }
</style>
</head>
<body>
<main class="letterhead">
  <header>
    <div class="brand">
      <span class="brand-mark"></span>
      <span class="brand-name">Brentholm</span>
    </div>

    <div class="contact-row row-address">
      <span class="item" style="left:0">
        <svg class="icon" viewBox="0 0 16 16"><path d="M8 15s5-5 5-9a5 5 0 0 0-10 0c0 4 5 9 5 9z"/><circle cx="8" cy="6" r="1.8"/></svg>
        <span><strong>Brentholm Pty Ltd.</strong> ABN 41 502 318 976 1120 Kingsford Road, Ashvale Vic. 3150</span>
      </span>
    </div>

    <div class="contact-row row-phone">
      <span class="item" style="left:0">
        <svg class="icon" viewBox="0 0 16 16"><path d="M3 2l3 1 1 3-2 1.5a9 9 0 0 0 3.5 4.5L10 10l3 1 1 3-2 1C7 14 2 9 2 4z"/></svg>
        <span>+61 3 9417 2830</span>
      </span>
      <span class="item" style="left:134px">
        <svg class="icon" viewBox="0 0 16 16"><rect x="4" y="1.5" width="8" height="4"/><rect x="1.5" y="5.5" width="13" height="6"/><rect x="4" y="9" width="8" height="5.5"/><path d="M6 11h4M6 12.8h4"/></svg>
        <span>+61 3 9417 2831</span>
      </span>
      <span class="item" style="left:269px">
        <svg class="icon" viewBox="0 0 16 16"><rect x="1.5" y="3.5" width="13" height="9"/><path d="M1.5 3.5L8 9l6.5-5.5"/></svg>
        <span>info@brentholm.com.au</span>
      </span>
    </div>

    <div class="contact-row row-web">
      <span class="item" style="left:0">
        <svg class="icon" viewBox="0 0 16 16"><circle cx="8" cy="8" r="6.5"/><ellipse cx="8" cy="8" rx="3" ry="6.5"/><path d="M1.5 8h13M2.5 4.8h11M2.5 11.2h11"/></svg>
        <span>www.brentholmaccountants.com.au</span>
      </span>
    </div>
  </header>

  <footer>
    <p class="est">EST. 1985</p>
    <div class="accreditations">
      <span class="badge-institute" role="img" aria-label="Professional institute membership badge"></span>
      <span class="badge-registered" role="img" aria-label="Registered tax agent badge"></span>
    </div>
    <div class="footer-band" role="img" aria-label="Decorative blue footer artwork in navy and sky blue tones"></div>
  </footer>
</main>
</body>
</html>
```